Silver Harbor Dental Clinic Flyer

I need to make a flyer Design for my clinic (Silver Harbor Dental Clinic) Based in Philippines, Makati .
We are Providing dental Service for high end market in the Philippines. Our speciality is Dental Aesthetic/Beautification. Our targets are actors/actresses, athletes, middle to high end
We are going to place this flyers in places like Ironvale Gym . and other lifestyle related places

Target Market(s)

Mid to high market

Industry/Entity Type

Dental Clinic

Font styles to use
Serif

Requirements
Must have
• The flyer should Contain Our address and the services that we offer
• #4873 Brightwell Plaza Makati Dalisay Cor. Marquez St. Vantage Park .Makati
• Email: info@silverharbor-example.com.ph
• mobile +639175550142
• Landline:(02)5550917
• instagram:@shdc.ph
• facebook:SHDC.ph
• Our Services :
• General Dentistry ,Orthodontics ,Cosmetic Dentistry ,Pediatric Dentistry ,Teeth Whitening,Dental Implants ,Wisdom Tooth Extraction,Root Canal Therapy
• Silver Harbor Kids Treatment:
• Teeth Cleaning , Flouride Application ,Tooth Colored Filing ,Extraction ,Pit and Fissure Sealants, Space Management
Nice to have
• Nice to have a nice tagline

```html
<!DOCTYPE html>
<html lang="en">
<head>
<meta charset="utf-8">
<title>Silver Harbor Dental Clinic Flyer</title>
<link href="https://fonts.googleapis.com/css2?family=Cinzel:wght@600&family=Crimson+Text:wght@700&family=Lato:wght@400;700&display=swap" rel="stylesheet">
<style>
  :root {
    --ink: #151a19;
    --slate: #5f7371;
    --slate-light: #8a9d9a;
    --paper: #ffffff;
    --text: #2f3333;
    --pill: #ececec;
  }
  * { margin: 0; padding: 0; box-sizing: border-box; }
  html, body { width: 1027px; height: 1200px; overflow: hidden; background: var(--paper); }
  .flyer { position: relative; width: 1027px; height: 1200px; background: var(--paper); font-family: 'Lato', sans-serif; color: var(--text); overflow: hidden; }
  .abs { position: absolute; }

  .hero-photo { left: 280px; top: 0; width: 747px; height: 441px;
    background: radial-gradient(ellipse at 62% 42%, #f3d6c6 0%, #e9c0ad 35%, #f6ebe5 70%, #ffffff 100%); }
  .brand-mark { left: 38px; top: 34px; width: 388px; height: 388px; border-radius: 50%;
    background: var(--ink); border: 6px solid #c9cfcf; display: flex; align-items: center; justify-content: center; text-align: center; }
  .brand-name { font-family: 'Cinzel', serif; font-weight: 600; font-size: 38px; line-height: 1.25; color: #a9b8b5; letter-spacing: 2px; }

  .tagline-band { left: 0; top: 441px; width: 1027px; height: 106px; }
  .tagline { left: 60px; top: 472px; width: 935px; text-align: right; font-family: 'Cinzel', serif; font-weight: 600; font-size: 49px; color: #fff; letter-spacing: 1px; line-height: 1; }

  .couple-photo { left: 0; top: 550px; width: 516px; height: 284px;
    background: linear-gradient(120deg, #c9d7a8 0%, #eadfcf 40%, #e8c9b4 65%, #f1ece6 100%); }
  .services { left: 516px; top: 555px; width: 511px; height: 279px; z-index: 2;
    background: linear-gradient(135deg, #6b7f7c 0%, #5c706e 55%, #70847f 100%); }
  .services-pill { left: 104px; top: 40px; width: 283px; height: 34px; border-radius: 17px; background: var(--pill);
    font-family: 'Crimson Text', serif; font-weight: 700; font-size: 25px; color: var(--ink); text-align: center; line-height: 34px; }
  .service-list { list-style: none; color: #fff; }
  .service-list li { position: relative; padding-left: 21px; }
  .service-list li::before { content: ""; position: absolute; left: 0; width: 11px; height: 11px; border-radius: 50%; background: #fff; }
  .service-list.main { left: 16px; top: 90px; font-size: 23px; }
  .service-list.main li { height: 35px; line-height: 35px; }
  .service-list.main li::before { top: 13px; }
  .service-list.extra { left: 292px; top: 94px; font-size: 20px; line-height: 26px; }
  .service-list.extra li { margin-bottom: 10px; }
  .service-list.extra li::before { top: 8px; }

  .divider { left: 0; top: 834px; width: 1027px; height: 18px; background: var(--ink); z-index: 2; }

  .kids-box { left: 49px; top: 872px; width: 478px; height: 130px; border: 4px solid var(--ink); border-radius: 12px; overflow: hidden; }
  .kids-title { height: 34px; background: linear-gradient(90deg, #101414, #39403f 60%, #101414);
    font-family: 'Crimson Text', serif; font-weight: 700; font-size: 25px; color: #fff; text-align: center; line-height: 34px; }
  .kids-list { list-style: none; display: grid; grid-template-columns: 219px 1fr; padding: 3px 0 0 12px; font-size: 17px; line-height: 28px; color: var(--text); }
  .kids-list li { display: flex; align-items: center; gap: 6px; }
  .tick { width: 12px; height: 12px; flex: none; }

  .follow { left: 52px; top: 1020px; display: flex; align-items: center; gap: 12px; }
  .follow-label { font-family: 'Crimson Text', serif; font-weight: 700; font-size: 28px; color: var(--slate); margin-right: 4px; }
  .social { display: flex; align-items: center; gap: 8px; font-size: 21px; color: var(--text); margin-right: 12px; }
  .social-square { width: 30px; height: 30px; border-radius: 5px; background: var(--slate); }

  .phone { left: 128px; font-size: 24px; font-weight: 700; color: #3a3d3d; }
  .phone.mobile { top: 1072px; }
  .phone.landline { top: 1106px; }

  .girl-photo { left: 626px; top: 852px; width: 356px; height: 297px;
    background: radial-gradient(ellipse at 55% 40%, #efd1bc 0%, #e4c2ab 30%, #9a9d9f 60%, #f5f5f5 85%); }

  .footer { left: 0; top: 1149px; width: 1027px; height: 51px; background: var(--ink); color: #fff; font-size: 15px; font-weight: 700; }
  .footer-address { position: absolute; left: 46px; top: 16px; }
  .footer-email { position: absolute; right: 22px; top: 16px; }
</style>
</head>
<body>
<main class="flyer">
  <div class="abs hero-photo" role="img" aria-label="Smiling young woman touching her cheek"></div>
  <div class="abs brand-mark"><span class="brand-name">Silver Harbor<br>Dental Clinic</span></div>

  <svg class="abs tagline-band" width="1027" height="106" viewBox="0 0 1027 106" aria-hidden="true">
    <defs>
      <linearGradient id="bandGrad" x1="0" x2="1" y1="0" y2="0">
        <stop offset="0" stop-color="#141918"/>
        <stop offset="0.35" stop-color="#2b3534"/>
        <stop offset="0.68" stop-color="#7d918e"/>
        <stop offset="0.82" stop-color="#3b4645"/>
        <stop offset="1" stop-color="#141918"/>
      </linearGradient>
    </defs>
    <path d="M0 106 C18 42 60 0 132 0 H1027 V106 Z" fill="url(#bandGrad)"/>
  </svg>
  <h1 class="abs tagline">Your Smile is Precious to Us</h1>

  <div class="abs couple-photo" role="img" aria-label="Smiling senior couple outdoors"></div>
  <section class="abs services">
    <h2 class="abs services-pill">OUR SERVICES:</h2>
    <ul class="abs service-list main">
      <li>General Dentistry ,</li>
      <li>Orthodontics ,</li>
      <li>Cosmetic Dentistry ,</li>
      <li>Pediatric Dentistry ,</li>
      <li>Dental Implants ,</li>
    </ul>
    <ul class="abs service-list extra">
      <li>Teeth Whitening,</li>
      <li>Root Canal<br>Therapy</li>
      <li>Wisdom Tooth<br>Extraction</li>
    </ul>
  </section>

  <div class="abs divider"></div>

  <section class="abs kids-box">
    <h2 class="kids-title">Silver Harbor Kids Treatment :</h2>
    <ul class="kids-list">
      <li><svg class="tick" viewBox="0 0 12 12"><path d="M1 6.5 L4.5 10 L11 2" fill="none" stroke="#4a5554" stroke-width="1.8"/></svg>Teeth Cleaning ,</li>
      <li><svg class="tick" viewBox="0 0 12 12"><path d="M1 6.5 L4.5 10 L11 2" fill="none" stroke="#4a5554" stroke-width="1.8"/></svg>Extraction ,</li>
      <li><svg class="tick" viewBox="0 0 12 12"><path d="M1 6.5 L4.5 10 L11 2" fill="none" stroke="#4a5554" stroke-width="1.8"/></svg>Flouride Application ,</li>
      <li><svg class="tick" viewBox="0 0 12 12"><path d="M1 6.5 L4.5 10 L11 2" fill="none" stroke="#4a5554" stroke-width="1.8"/></svg>Pit and Fissure Sealants,</li>
      <li><svg class="tick" viewBox="0 0 12 12"><path d="M1 6.5 L4.5 10 L11 2" fill="none" stroke="#4a5554" stroke-width="1.8"/></svg>Tooth Colored Filing ,</li>
      <li><svg class="tick" viewBox="0 0 12 12"><path d="M1 6.5 L4.5 10 L11 2" fill="none" stroke="#4a5554" stroke-width="1.8"/></svg>Space Management</li>
    </ul>
  </section>

  <div class="abs follow">
    <span class="follow-label">Follow us on :</span>
    <span class="social"><span class="social-square"></span>@shdc.ph</span>
    <span class="social"><span class="social-square"></span>SHDC.ph</span>
  </div>
  <p class="abs phone mobile">MOBILE : +639175550142</p>
  <p class="abs phone landline">LANDLINE:&nbsp; (02)5550917</p>

  <div class="abs girl-photo" role="img" aria-label="Smiling young woman in a scarf giving a thumbs up"></div>

  <footer class="abs footer">
    <span class="footer-address">#4873 Brightwell Plaza Makati Dalisay Cor. Marquez St. Vantage Park .Makati</span>
    <span class="footer-email">Email: info@silverharbor-example.com.ph</span>
  </footer>
</main>
</body>
</html>
```